Property Developer - Simple yet Sophisticated and Sharp Business Card

We are a medium sized property developer involved mainly in townhouse developments and land subdivisions.

The company is looking for a simple, sharp and sophisticated business card that will be given to contractors, land owners, financiers etc and thus will need to look professional.

Property development related graphics and art can be used, however the card is not to be too "busy" or crowded. Our company name is KL Estates which could possibly be incorporated into the graphics or artwork.

Single sided and/or double sided designs will be acceptable.

A Simple, Sophisticated, Sharp design please!

Good Luck !

```html
<!DOCTYPE html>
<html lang="en">
<head>
<meta charset="utf-8">
<title>KL Estates – Business Card Set</title>
<link rel="stylesheet" href="https://fonts.googleapis.com/css2?family=Arimo:wght@400;700&display=swap">
<style>
  :root {
    --backdrop: #3b3b3b;
    --card-white: #ffffff;
    --brand-green: #3cb54a;
    --green-light: #8dc63f;
    --green-deep: #27ae4c;
    --text-dark: #222222;
    --shadow: rgba(0, 0, 0, 0.35);
  }
  * { box-sizing: border-box; margin: 0; padding: 0; }
  html, body {
    width: 1200px; height: 900px; overflow: hidden;
    background: var(--backdrop);
    font-family: "Arimo", Arial, sans-serif;
  }
  .canvas { position: relative; width: 1200px; height: 900px; }
  .card {
    position: absolute;
    background: var(--card-white);
    box-shadow: 0 3px 10px var(--shadow);
  }
  .card--back-plain { left: 40px; top: 80px; width: 550px; height: 294px; }
  .card--back-green {
    left: 615px; top: 80px; width: 548px; height: 294px;
    background: radial-gradient(ellipse at center, var(--green-light) 0%, #6fc043 45%, var(--green-deep) 100%);
  }
  .card--front { left: 210px; top: 504px; width: 656px; height: 351px; }

  .wordmark {
    color: var(--brand-green);
    font-weight: 700;
    letter-spacing: -1px;
    white-space: nowrap;
  }
  .logo-tile {
    position: absolute; left: 118px; top: 66px; width: 284px; height: 162px;
    background: var(--card-white);
    border-radius: 22px;
    box-shadow: 0 6px 16px var(--shadow);
    display: flex; align-items: center; justify-content: center;
  }
  .logo-disc {
    position: absolute; left: 50%; top: 50%;
    width: 234px; height: 234px; margin: -117px 0 0 -117px;
    background: var(--card-white); border-radius: 50%;
    box-shadow: 0 4px 14px rgba(0,0,0,0.25);
    display: flex; align-items: center; justify-content: center;
  }
  .logo-tile .wordmark, .logo-disc .wordmark { font-size: 40px; }

  .front-logo {
    position: absolute; top: 36px; left: 0; width: 100%;
    text-align: center;
  }
  .front-logo .wordmark { font-size: 54px; }

  .person {
    position: absolute; top: 196px; left: 0; width: 100%;
    text-align: center;
  }
  .person__name { color: var(--brand-green); font-weight: 700; font-size: 20px; }
  .person__role { color: #1e7a32; font-weight: 700; font-size: 12px; margin-top: 4px; }

  .contact {
    position: absolute; left: 0; width: 100%;
    display: flex; justify-content: center; align-items: center; gap: 10px;
    font-size: 16px; color: var(--text-dark);
  }
  .contact--lines { top: 294px; }
  .contact--address { top: 318px; }
  .contact__item { display: inline-flex; align-items: center; gap: 4px; }
  .contact__icon { width: 18px; height: 14px; fill: var(--brand-green); }
  .contact__label { color: var(--brand-green); font-weight: 700; }
</style>
</head>
<body>
<main class="canvas">

  <section class="card card--back-plain" aria-label="Card back, white">
    <div class="logo-tile"><span class="wordmark">KL Estates</span></div>
  </section>

  <section class="card card--back-green" aria-label="Card back, green">
    <div class="logo-disc"><span class="wordmark">KL Estates</span></div>
  </section>

  <section class="card card--front" aria-label="Card front">
    <div class="front-logo"><span class="wordmark">KL Estates</span></div>

    <div class="person">
      <p class="person__name">Your Name Here</p>
      <p class="person__role">Principal</p>
    </div>

    <div class="contact contact--lines">
      <span class="contact__item">
        <svg class="contact__icon" viewBox="0 0 18 14" aria-hidden="true">
          <path d="M2 4 Q9 -1 16 4 L14 6 L12 4 Q9 3 6 4 L4 6 Z"/>
          <rect x="4" y="6" width="10" height="7" rx="1"/>
        </svg>(07) 3900 4521
      </span>
      <span class="contact__item">
        <svg class="contact__icon" viewBox="0 0 18 14" aria-hidden="true">
          <rect x="3" y="2" width="12" height="8" rx="1" fill="none" stroke="#3cb54a" stroke-width="1.6"/>
          <rect x="1" y="11" width="16" height="2"/>
        </svg>(07) 3900 4522
      </span>
      <span class="contact__item">
        <span class="contact__label">E</span> projects@klestates.com.au
      </span>
    </div>

    <div class="contact contact--address">
      <span class="contact__item">
        <svg class="contact__icon" viewBox="0 0 18 14" aria-hidden="true">
          <rect x="1" y="2" width="16" height="10" rx="2"/>
        </svg>PO Box 2815 Eastwood Park QLD 4120
      </span>
    </div>
  </section>

</main>
</body>
</html>
```